Veterinary Hospital Brochure - 2 Drafts - 1 Normal and 1 Fun.

Meadowbrook Pet Hospital needs a brochure to promote our veterinary hospital. These will be delivered to local mailboxes. I would like to see atleast 2 submissions from each designer.
One submission conservative and A4 folded DL and another submission more radical and interesting with innovative folding or crazy concepts. Maybe the brochure could be designed to fold into a dog house ?
I want at least one version to be VERY SIMPLE AND INTIMATE.
Our existing website is here: http://furlane.example/ and our new website will look like this: http://trial4.pagemint.example/#home
Please use colors and images from the new website, and information from the old website. The heading font used in the new site is Qorvatype - Otter Tilt Sketchline
I want the brochure to be simple and engaging on first view, and then provide the opportunity to find more information if desired. The brochure needs to be captivating on the outside so people don't throw it away immediately.

We will soon need letterhead, flags, pens, business cards, signs and vouchers so there is the opportunity for more work for the successful designer.

Target Market(s)

Women 25 to 44

Industry/Entity Type

Veterinary

Contact Information for Business Card

Meadowbrook Pet Hospital
14 Marlow Crescent
Tamsworth Vale
NSW 2417
Phone: 02 61938205
Emergency: 0417360592
Fax: 02 83159462
www.meadowbrookvets.example
contact@meadowbrookvets.example

Font styles to use
Script

Requirements
Must have
• Colors from the new website: http://meadowbrookvets.example/ and new logo.
• Information from the old website: http://furlane.example/
• 2 drafts - A normal A4 folded DL flyer and an interesting crazy design.
Nice to have
• VERY SIMPLE
• Subdued
• Intimate
Should not have
• Intense colours
• Red

```html
<!DOCTYPE html>
<html lang="en">
<head>
<meta charset="utf-8">
<title>Meadowbrook Pet Hospital – Trifold Brochure</title>
<link href="https://fonts.googleapis.com/css2?family=Catamaran:wght@400;500;600;700&display=swap" rel="stylesheet">
<style>
:root{
  --page:#efe7dc;
  --orange:#f38f4f;
  --orange-deep:#ec7f3c;
  --green:#7a9a45;
  --green-light:#93ad5d;
  --ink:#333;
  --white:#fff;
}
*{box-sizing:border-box;margin:0;padding:0}
html,body{width:869px;height:1200px;overflow:hidden;background:var(--page)}
body{position:relative;font-family:'Catamaran',sans-serif;color:var(--ink)}
.sheet{position:absolute;left:63px;width:719px;overflow:hidden;background:var(--white)}
.sheet--outside{top:62px;height:508px}
.sheet--inside{top:629px;height:509px}
.layer{position:absolute;inset:0}
.abs{position:absolute}
.photo{position:absolute}
.heading{font-weight:600;font-size:14px;letter-spacing:.2px;padding-bottom:4px;border-bottom:1px solid currentColor;width:172px}
.heading--light{color:var(--white);border-color:rgba(255,255,255,.8)}
.heading--orange{color:var(--orange-deep);border-color:#bbb}
.copy{font-size:9.4px;line-height:12px;text-align:justify}
.copy p+p{margin-top:10px}
.copy--light{color:var(--white)}
.brand{font-weight:700;color:#5a4a3a;text-align:center;line-height:1.05}
.brand-mark{display:inline-block;width:9px;height:9px;border-radius:50%;background:var(--orange);margin-right:5px;vertical-align:middle}
.contact{text-align:center;font-size:10.4px;line-height:13.5px}
.contact .name{color:var(--green);font-weight:500;font-size:11.5px}
.contact .web{color:var(--orange-deep);font-weight:600}
.services{list-style:none;font-size:10.4px;color:var(--white)}
.services li{height:21px;display:flex;align-items:center;white-space:nowrap}
.paw{width:9px;height:9px;margin-right:8px;flex:none}
.url-band{color:var(--white);font-weight:600;font-size:11px}
.footer-bar{background:rgba(122,154,69,.92);color:var(--white);font-size:11.5px;line-height:33px;padding-left:14px;white-space:nowrap}
.footer-bar b{font-weight:700}
</style>
</head>
<body>

<section class="sheet sheet--outside">
  <svg class="layer" width="719" height="508" viewBox="0 0 719 508">
    <defs>
      <linearGradient id="g-cat" x1="0" y1="0" x2="0" y2="1"><stop offset="0" stop-color="#c9b9a8"/><stop offset="1" stop-color="#8f7f70"/></linearGradient>
      <linearGradient id="g-kiss" x1="0" y1="0" x2="1" y2="1"><stop offset="0" stop-color="#cdbfae"/><stop offset=".5" stop-color="#d9c3a2"/><stop offset="1" stop-color="#8c8a84"/></linearGradient>
    </defs>
    <rect x="0" y="0" width="239" height="508" fill="var(--orange)"/>
    <path d="M0 478 Q120 462 239 470 V508 H0Z" fill="var(--green-light)"/>
    <rect x="239" y="0" width="241" height="508" fill="var(--white)"/>
    <path d="M239 0 H480 V150 Q390 215 239 170Z" fill="url(#g-cat)"/>
    <path d="M239 170 Q390 215 480 150 L480 158 Q390 224 239 178Z" fill="var(--green)"/>
    <path d="M239 490 Q330 472 430 505 L430 508 H239Z" fill="var(--green-light)" opacity=".8"/>
    <path d="M480 0 H719 V415 Q620 350 480 400Z" fill="url(#g-kiss)"/>
    <path d="M480 400 Q620 350 719 415 V425 Q620 362 480 410Z" fill="var(--orange)"/>
    <path d="M480 500 Q600 465 719 475 V508 H480Z" fill="var(--green)"/>
  </svg>

  <div class="photo" role="img" aria-label="Woman stroking a tabby cat on a table" style="left:239px;top:0;width:241px;height:150px"></div>
  <div class="photo" role="img" aria-label="Smiling woman kissing a French bulldog" style="left:480px;top:0;width:239px;height:395px"></div>

  <div class="abs" style="left:16px;top:22px;width:211px">
    <h2 class="heading heading--light">OUR MISSION</h2>
    <div class="copy copy--light" style="margin-top:9px">
      <p>Meadowbrook Pet Hospital is a companion animal veterinary Hospital in Tamsworth Vale. We treat Dogs, Cats, Reptiles, Rodents, Birds, and other little critters. As a companion animal only Hospital, we are dedicated to improving the well-being of your beloved pets. We think they are part of the family and should receive the absolute best possible care.</p>
      <p>Meadowbrook Pet Hospital is a Companion Animal Veterinary Hospital in Tamsworth committed to providing excellent care for loved pets and their owners.</p>
      <p style="text-align:left">To achieve this we:<br>• Provide a welcoming environment.<br>• Treat all patients and owners as important.<br>• Educate owners to help prevent illness.<br>• When illness occurs, treat with the latest<br>&nbsp;&nbsp;&nbsp;equipment and techniques.</p>
    </div>
  </div>
  <div class="photo" role="img" aria-label="Golden puppy nuzzling a grey kitten" style="left:8px;top:310px;width:226px;height:190px;background:linear-gradient(160deg,rgba(240,200,150,.9),rgba(200,170,140,.9));border-radius:45% 45% 8px 8px"></div>

  <div class="brand abs" style="left:239px;top:236px;width:241px;font-size:17px"><span class="brand-mark"></span>MEADOWBROOK<br>PET HOSPITAL</div>
  <div class="photo" role="img" aria-label="Street map showing the hospital location" style="left:261px;top:279px;width:200px;height:100px;background:linear-gradient(135deg,#eef0f2,#dde3e6);border:3px solid var(--white);box-shadow:0 1px 4px rgba(0,0,0,.25)"></div>
  <div class="contact abs" style="left:239px;top:401px;width:241px">
    <div class="name">MEADOWBROOK PET HOSPITAL</div>
    <div>14 Marlow Cres Tamsworth Vale NSW 2417.</div>
    <div>Phone: 02 6193 8205</div>
    <div>contact@furlane.example</div>
    <div class="web">www.meadowbrookvets.example</div>
  </div>

  <div class="brand abs" style="left:480px;top:410px;width:239px;font-size:19px"><span class="brand-mark"></span>MEADOWBROOK<br>PET HOSPITAL</div>
  <div class="url-band abs" style="left:480px;top:484px;width:239px;text-align:center;padding-left:20px">www.meadowbrookvets.example</div>
</section>

<section class="sheet sheet--inside">
  <svg class="layer" width="719" height="509" viewBox="0 0 719 509">
    <defs>
      <linearGradient id="g-hug" x1="0" y1="0" x2="1" y2="0"><stop offset="0" stop-color="#c7b29c"/><stop offset=".5" stop-color="#a98d73"/><stop offset="1" stop-color="#6e6d6f"/></linearGradient>
      <linearGradient id="g-grey" x1="0" y1="0" x2="1" y2="0"><stop offset="0" stop-color="#e9e9e9"/><stop offset="1" stop-color="#fbfbfb"/></linearGradient>
      <linearGradient id="g-vet" x1="0" y1="0" x2="1" y2="1"><stop offset="0" stop-color="#9a8c80"/><stop offset="1" stop-color="#d8d2cc"/></linearGradient>
    </defs>
    <rect x="0" y="0" width="239" height="509" fill="url(#g-grey)"/>
    <rect x="239" y="0" width="480" height="509" fill="var(--orange)"/>
    <path d="M245 0 Q270 95 380 140 Q540 205 719 175 V0Z" fill="var(--green)"/>
    <path d="M255 0 Q280 90 385 132 Q540 195 719 166 V0Z" fill="url(#g-hug)"/>
    <path d="M410 509 Q480 370 719 330 V509Z" fill="var(--green)"/>
    <path d="M418 509 Q488 378 719 340 V509Z" fill="url(#g-vet)"/>
    <circle cx="659" cy="169" r="49" fill="var(--green-light)"/>
    <circle cx="659" cy="169" r="46" fill="var(--white)"/>
    <circle cx="659" cy="169" r="40" fill="#d9c1a4"/>
  </svg>
  <div class="photo" role="img" aria-label="Woman hugging a black and tan dog" style="left:255px;top:0;width:464px;height:160px"></div>
  <div class="photo" role="img" aria-label="Beagle puppy sitting" style="left:619px;top:129px;width:80px;height:80px;border-radius:50%"></div>
  <div class="photo" role="img" aria-label="Vets examining a dog on the clinic floor" style="left:430px;top:345px;width:289px;height:164px"></div>

  <div class="abs" style="left:14px;top:30px;width:211px">
    <h2 class="heading heading--orange">ABOUT US</h2>
    <div class="copy" style="margin-top:9px">
      <p>Meadowbrook Pet Hospital is built on the grounds of a chapel in 1897. The chapel hall has been converted into a beautiful reception area.</p>
      <p>We have constructed a modern veterinary hospital with small animal surgical facilities, X-ray, ultrasound, dog and cat wards, laboratory, isolation, multiple consultation rooms and a huge treatment area.</p>
      <p style="text-align:left">Come in for a tour of our facility or go online:<br><b style="color:var(--green)">www.meadowbrookvets.example</b></p>
    </div>
  </div>
  <div class="photo" role="img" aria-label="Golden retriever lying with a ginger cat" style="left:10px;top:220px;width:220px;height:245px;background:linear-gradient(160deg,#f1d4ae,#d9a672);border-radius:50% 50% 10px 10px"></div>
  <div class="footer-bar abs" style="left:0;top:464px;width:391px;height:33px">For emergency pet care, please contact <b>MEADOWBROOK PET HOSPITAL</b></div>

  <h2 class="abs" style="left:307px;top:172px;color:var(--white);font-weight:600;font-size:14px">OUR SERVICES</h2>
  <ul class="services abs" style="left:254px;top:202px">
    <li><svg class="paw" viewBox="0 0 10 10"><circle cx="5" cy="6.5" r="2.8" fill="#fff"/><circle cx="1.6" cy="3.4" r="1.2" fill="#fff"/><circle cx="3.8" cy="1.6" r="1.2" fill="#fff"/><circle cx="6.2" cy="1.6" r="1.2" fill="#fff"/><circle cx="8.4" cy="3.4" r="1.2" fill="#fff"/></svg>Puppy Pre-School</li>
    <li><svg class="paw" viewBox="0 0 10 10"><circle cx="5" cy="6.5" r="2.8" fill="#fff"/><circle cx="1.6" cy="3.4" r="1.2" fill="#fff"/><circle cx="3.8" cy="1.6" r="1.2" fill="#fff"/><circle cx="6.2" cy="1.6" r="1.2" fill="#fff"/><circle cx="8.4" cy="3.4" r="1.2" fill="#fff"/></svg>Vaccinations</li>
    <li><svg class="paw" viewBox="0 0 10 10"><circle cx="5" cy="6.5" r="2.8" fill="#fff"/><circle cx="1.6" cy="3.4" r="1.2" fill="#fff"/><circle cx="3.8" cy="1.6" r="1.2" fill="#fff"/><circle cx="6.2" cy="1.6" r="1.2" fill="#fff"/><circle cx="8.4" cy="3.4" r="1.2" fill="#fff"/></svg>Microchipping</li>
    <li><svg class="paw" viewBox="0 0 10 10"><circle cx="5" cy="6.5" r="2.8" fill="#fff"/><circle cx="1.6" cy="3.4" r="1.2" fill="#fff"/><circle cx="3.8" cy="1.6" r="1.2" fill="#fff"/><circle cx="6.2" cy="1.6" r="1.2" fill="#fff"/><circle cx="8.4" cy="3.4" r="1.2" fill="#fff"/></svg>De-sexing</li>
    <li><svg class="paw" viewBox="0 0 10 10"><circle cx="5" cy="6.5" r="2.8" fill="#fff"/><circle cx="1.6" cy="3.4" r="1.2" fill="#fff"/><circle cx="3.8" cy="1.6" r="1.2" fill="#fff"/><circle cx="6.2" cy="1.6" r="1.2" fill="#fff"/><circle cx="8.4" cy="3.4" r="1.2" fill="#fff"/></svg>Dental Care</li>
    <li><svg class="paw" viewBox="0 0 10 10"><circle cx="5" cy="6.5" r="2.8" fill="#fff"/><circle cx="1.6" cy="3.4" r="1.2" fill="#fff"/><circle cx="3.8" cy="1.6" r="1.2" fill="#fff"/><circle cx="6.2" cy="1.6" r="1.2" fill="#fff"/><circle cx="8.4" cy="3.4" r="1.2" fill="#fff"/></svg>Caeserian</li>
    <li><svg class="paw" viewBox="0 0 10 10"><circle cx="5" cy="6.5" r="2.8" fill="#fff"/><circle cx="1.6" cy="3.4" r="1.2" fill="#fff"/><circle cx="3.8" cy="1.6" r="1.2" fill="#fff"/><circle cx="6.2" cy="1.6" r="1.2" fill="#fff"/><circle cx="8.4" cy="3.4" r="1.2" fill="#fff"/></svg>Behaviour Consults</li>
    <li><svg class="paw" viewBox="0 0 10 10"><circle cx="5" cy="6.5" r="2.8" fill="#fff"/><circle cx="1.6" cy="3.4" r="1.2" fill="#fff"/><circle cx="3.8" cy="1.6" r="1.2" fill="#fff"/><circle cx="6.2" cy="1.6" r="1.2" fill="#fff"/><circle cx="8.4" cy="3.4" r="1.2" fill="#fff"/></svg>Aged Care Consults</li>
    <li><svg class="paw" viewBox="0 0 10 10"><circle cx="5" cy="6.5" r="2.8" fill="#fff"/><circle cx="1.6" cy="3.4" r="1.2" fill="#fff"/><circle cx="3.8" cy="1.6" r="1.2" fill="#fff"/><circle cx="6.2" cy="1.6" r="1.2" fill="#fff"/><circle cx="8.4" cy="3.4" r="1.2" fill="#fff"/></svg>Nutrition Advice</li>
    <li><svg class="paw" viewBox="0 0 10 10"><circle cx="5" cy="6.5" r="2.8" fill="#fff"/><circle cx="1.6" cy="3.4" r="1.2" fill="#fff"/><circle cx="3.8" cy="1.6" r="1.2" fill="#fff"/><circle cx="6.2" cy="1.6" r="1.2" fill="#fff"/><circle cx="8.4" cy="3.4" r="1.2" fill="#fff"/></svg>Flea Treatments</li>
  </ul>
  <ul class="services abs" style="left:368px;top:202px">
    <li><svg class="paw" viewBox="0 0 10 10"><circle cx="5" cy="6.5" r="2.8" fill="#fff"/><circle cx="1.6" cy="3.4" r="1.2" fill="#fff"/><circle cx="3.8" cy="1.6" r="1.2" fill="#fff"/><circle cx="6.2" cy="1.6" r="1.2" fill="#fff"/><circle cx="8.4" cy="3.4" r="1.2" fill="#fff"/></svg>Emergency Surgery</li>
    <li><svg class="paw" viewBox="0 0 10 10"><circle cx="5" cy="6.5" r="2.8" fill="#fff"/><circle cx="1.6" cy="3.4" r="1.2" fill="#fff"/><circle cx="3.8" cy="1.6" r="1.2" fill="#fff"/><circle cx="6.2" cy="1.6" r="1.2" fill="#fff"/><circle cx="8.4" cy="3.4" r="1.2" fill="#fff"/></svg>Radiology</li>
    <li><svg class="paw" viewBox="0 0 10 10"><circle cx="5" cy="6.5" r="2.8" fill="#fff"/><circle cx="1.6" cy="3.4" r="1.2" fill="#fff"/><circle cx="3.8" cy="1.6" r="1.2" fill="#fff"/><circle cx="6.2" cy="1.6" r="1.2" fill="#fff"/><circle cx="8.4" cy="3.4" r="1.2" fill="#fff"/></svg>Ultrasound</li>
    <li><svg class="paw" viewBox="0 0 10 10"><circle cx="5" cy="6.5" r="2.8" fill="#fff"/><circle cx="1.6" cy="3.4" r="1.2" fill="#fff"/><circle cx="3.8" cy="1.6" r="1.2" fill="#fff"/><circle cx="6.2" cy="1.6" r="1.2" fill="#fff"/><circle cx="8.4" cy="3.4" r="1.2" fill="#fff"/></svg>Routine Blood Tests</li>
    <li><svg class="paw" viewBox="0 0 10 10"><circle cx="5" cy="6.5" r="2.8" fill="#fff"/><circle cx="1.6" cy="3.4" r="1.2" fill="#fff"/><circle cx="3.8" cy="1.6" r="1.2" fill="#fff"/><circle cx="6.2" cy="1.6" r="1.2" fill="#fff"/><circle cx="8.4" cy="3.4" r="1.2" fill="#fff"/></svg>Orthopaedic Surgery</li>
    <li><svg class="paw" viewBox="0 0 10 10"><circle cx="5" cy="6.5" r="2.8" fill="#fff"/><circle cx="1.6" cy="3.4" r="1.2" fill="#fff"/><circle cx="3.8" cy="1.6" r="1.2" fill="#fff"/><circle cx="6.2" cy="1.6" r="1.2" fill="#fff"/><circle cx="8.4" cy="3.4" r="1.2" fill="#fff"/></svg>Cruiciate Repair</li>
    <li><svg class="paw" viewBox="0 0 10 10"><circle cx="5" cy="6.5" r="2.8" fill="#fff"/><circle cx="1.6" cy="3.4" r="1.2" fill="#fff"/><circle cx="3.8" cy="1.6" r="1.2" fill="#fff"/><circle cx="6.2" cy="1.6" r="1.2" fill="#fff"/><circle cx="8.4" cy="3.4" r="1.2" fill="#fff"/></svg>Grieving Support</li>
    <li><svg class="paw" viewBox="0 0 10 10"><circle cx="5" cy="6.5" r="2.8" fill="#fff"/><circle cx="1.6" cy="3.4" r="1.2" fill="#fff"/><circle cx="3.8" cy="1.6" r="1.2" fill="#fff"/><circle cx="6.2" cy="1.6" r="1.2" fill="#fff"/><circle cx="8.4" cy="3.4" r="1.2" fill="#fff"/></svg>Skin Treatments</li>
  </ul>

  <div class="abs" style="left:498px;top:206px;width:205px">
    <h2 class="heading heading--light" style="width:130px">PUPY CLASES</h2>
    <div class="copy copy--light" style="margin-top:14px">Meadowbrook Pet Hospital runs a 5 week puppy class. These are great fun and provide essential socialisation and training for you and your puppy. The classes prevent a range of behavioural issues and are an essential part prevention is better than cure philasophy.</div>
  </div>
</section>

</body>
</html>
```